Tavelin Global Kft. is an online recruitment marketplace connecting the employers and recruiters together. We provide an e-bussiness solution for companies and give busines opportunity for recruiters.
We have a logo design already, which should be used on the business card.
Our colours are grey and magenta, which can be seen in the logo. Black is also welcome.
The style should be dynamic, young but professional. It should be clear, visible, elegant, not too crowded, simple but exciting.
We need the following data on the BC: name, title, address, phone,fax and mobile number, email address, website.
Target Market(s)
Our target market are companies, as this is a B2B business. We also target recruiters, recruitment professionals, headhunters.We would like to be impressive and different.
Industry/Entity Type
Business
Requirements
Must have
- We would like to promote our website, www.tavelglob.hu.
- Please, put this on the back with a quite visible letter size.The style should be dynamic, young but professional. It should be clear, visible, elegant, not too crowded, simple but exciting.
Should not have
- We do not want to see people figures.

```html
<!DOCTYPE html>
<html lang="en">
<head>
<meta charset="utf-8">
<title>Tavelin Global Kft. – Business Card</title>
<link rel="stylesheet" href="https://fonts.googleapis.com/css2?family=Arimo:wght@400;700&display=swap">
<style>
  :root {
    --page: #f2f2f2;
    --card: #ffffff;
    --magenta: #b81e78;
    --name-grey: #7a687a;
    --text-grey: #6a5e6c;
    --tone-light: #f2d0dc;
    --tone-mid: #dfa0b8;
    --tone-deep: #a8467f;
  }
  html, body {
    margin: 0;
    width: 1200px;
    height: 900px;
    overflow: hidden;
    background: var(--page);
    font-family: "Arimo", Arial, sans-serif;
  }
  .card {
    position: absolute;
    left: 70px;
    top: 131px;
    width: 1060px;
    height: 637px;
    background: var(--card);
    box-shadow: 0 0 0 1px #d8d8d8;
  }
  .corner-accent { position: absolute; left: 0; top: 0; }
  .holder {
    position: absolute;
    left: 552px;
    top: 148px;
    transform: translateX(-50%);
    text-align: center;
  }
  .holder-name {
    margin: 0;
    font-size: 39px;
    font-weight: 400;
    color: var(--name-grey);
    padding: 0 2px 4px;
    border-bottom: 3px solid var(--name-grey);
    line-height: 1.1;
  }
  .holder-title {
    margin: 6px 0 0;
    font-size: 18px;
    color: var(--magenta);
  }
  .contact {
    position: absolute;
    left: 282px;
    top: 272px;
    display: grid;
    grid-template-columns: 144px auto;
    font-size: 22px;
    line-height: 28px;
    margin: 0;
  }
  .contact dt { color: var(--magenta); }
  .contact dd { margin: 0; color: var(--text-grey); white-space: nowrap; }
  .brand {
    position: absolute;
    left: 32px;
    top: 424px;
    display: flex;
    align-items: flex-end;
    gap: 16px;
  }
  .brand-square {
    width: 170px;
    height: 170px;
    background: var(--magenta);
  }
  .brand-name {
    font-size: 33px;
    font-weight: 700;
    color: var(--magenta);
    line-height: 1;
    margin-bottom: 14px;
    white-space: nowrap;
  }
</style>
</head>
<body>
  <article class="card">
    <svg class="corner-accent" width="1060" height="360" viewBox="0 0 1060 360" role="img" aria-label="Decorative tile mosaic area in pink, grey and magenta tones">
      <defs>
        <linearGradient id="accentFill" x1="0" y1="1" x2="1" y2="0">
          <stop offset="0" stop-color="var(--tone-light)"/>
          <stop offset="0.6" stop-color="var(--tone-mid)"/>
          <stop offset="1" stop-color="var(--tone-deep)"/>
        </linearGradient>
      </defs>
      <polygon points="717,22 1033,22 1033,339" fill="url(#accentFill)"/>
    </svg>

    <header class="holder">
      <h1 class="holder-name">Marek Halden</h1>
      <p class="holder-title">Branch Manager</p>
    </header>

    <dl class="contact">
      <dt>Addres</dt>
      <dd>: Lindenweg 42 Corvin Tower 7th floor,<br>&nbsp;&nbsp;Central District, Budapest 1082</dd>
      <dt>Phone / Fax</dt>
      <dd>: +36 (01) 55408217, 55408218</dd>
      <dt>Mobile</dt>
      <dd>: +36309471582</dd>
      <dt>e-mail</dt>
      <dd>: marek_h@tavelglob.hu</dd>
      <dt>website</dt>
      <dd>: http://www.tavelglob.hu</dd>
    </dl>

    <div class="brand">
      <div class="brand-square" aria-hidden="true"></div>
      <span class="brand-name">Tavelin Global Kft.</span>
    </div>
  </article>
</body>
</html>
```